Business card for Luxury Portable Restroom Trailer company

We are a Luxury Portable Restroom Trailer Company Called PELIKAR HIRES. Based in Orange County California. We provide portable restroom trailers for events, such as, Weddings, Concerts, Charity events, Sporting events, Tournaments, Corporate events, ect. We rent and Sell the Luxury restrooms. Our colors are white, grey, and Orange. As you will see in the logo we uploaded.
There are 2 people in the company so the names and titles will change for the 3 people but card will remain the same. Here is the information for each Person: Dennis Moyle CFO 555 018-3647
next Person: Wesley Tanford VP 555 018-3647
Next Person: Miles Tanford CEO 555 018-3647
Information to include on the card: Luxury Restroom Trailers Rental and Sales. Weddings, Concerts, Charity, Sporting and Corp. Events.

```html
<!DOCTYPE html>
<html lang="en">
<head>
<meta charset="utf-8">
<title>Pelikar Hires – Business Card</title>
<link rel="stylesheet" href="https://fonts.googleapis.com/css2?family=Montserrat:wght@500;600;800&display=swap">
<style>
  :root {
    --bg: #dcdcdc;
    --charcoal: #4a4a4c;
    --orange: #e8611c;
    --white: #ffffff;
    --paper: #f6f6f6;
    --ink: #4a4a4c;
  }
  * { box-sizing: border-box; margin: 0; padding: 0; }
  html, body { width: 1200px; height: 800px; overflow: hidden; }
  body {
    background: var(--bg);
    font-family: "Montserrat", Arial, sans-serif;
    display: flex;
    align-items: center;
    justify-content: center;
    gap: 60px;
  }
  .card {
    position: relative;
    width: 520px;
    height: 300px;
    border-radius: 20px;
    overflow: hidden;
    box-shadow: 0 4px 0 var(--orange), 0 14px 28px rgba(0,0,0,.22);
  }

  /* Contact side */
  .card--contact { background: var(--paper); }
  .card--contact .split { position: absolute; inset: 0; }
  .card--contact .brand {
    position: absolute;
    left: 34px;
    top: 128px;
    display: flex;
    align-items: center;
    gap: 8px;
    color: var(--ink);
    font-weight: 800;
    font-size: 22px;
    letter-spacing: 1px;
  }
  .brand-square {
    width: 14px; height: 14px;
    background: var(--orange);
  }
  .details {
    position: absolute;
    right: 28px;
    top: 34px;
    width: 210px;
    text-align: right;
    color: var(--white);
  }
  .details .name {
    color: var(--orange);
    font-weight: 800;
    font-size: 21px;
    letter-spacing: .5px;
    text-transform: uppercase;
  }
  .details .title {
    font-size: 12px;
    font-weight: 500;
    margin-bottom: 22px;
  }
  .details .address {
    font-size: 12px;
    font-weight: 500;
    line-height: 1.45;
    margin-bottom: 14px;
  }
  .contact-line {
    display: flex;
    justify-content: flex-end;
    align-items: center;
    gap: 6px;
    font-size: 12px;
    font-weight: 500;
    line-height: 1.6;
  }
  .contact-line svg { width: 11px; height: 11px; flex: none; }

  /* Brand side */
  .card--brand {
    background: var(--charcoal);
    color: var(--white);
    display: flex;
    flex-direction: column;
    align-items: center;
    justify-content: center;
    gap: 34px;
  }
  .card--brand .brand {
    display: flex;
    align-items: center;
    gap: 14px;
    font-weight: 800;
    font-size: 40px;
    letter-spacing: 2px;
    color: var(--white);
  }
  .card--brand .brand-square { width: 24px; height: 24px; }
  .tagline {
    text-align: center;
    font-size: 15px;
    font-weight: 500;
    line-height: 1.5;
  }
</style>
</head>
<body>

  <section class="card card--contact" aria-label="Business card, contact side">
    <svg class="split" viewBox="0 0 520 300" preserveAspectRatio="none" aria-hidden="true">
      <polygon points="250,0 262,0 322,300 308,300" fill="#e8611c"/>
      <polygon points="272,0 520,0 520,300 334,300" fill="#4a4a4c"/>
    </svg>

    <div class="brand"><span class="brand-square"></span>PELIKAR HIRES</div>

    <div class="details">
      <p class="name">Dennis Moyle</p>
      <p class="title">CFO</p>
      <p class="address">2710 Harbor Crest Lane<br>Costa Mesa, CA 92626</p>
      <p class="contact-line">555 018-3647
        <svg viewBox="0 0 12 12"><path fill="#e8611c" d="M2.5 1 4.4 1.2 5 3.6 3.8 4.6A6.5 6.5 0 0 0 7.4 8.2L8.4 7 10.8 7.6 11 9.5 9.8 11C5.4 11 1 6.6 1 2.2Z"/></svg>
      </p>
      <p class="contact-line">name@PELIKAR.com
        <svg viewBox="0 0 12 12"><rect x="0.5" y="2" width="11" height="8" fill="#e8611c"/><path d="M1 2.5 6 6.5 11 2.5" stroke="#4a4a4c" fill="none"/></svg>
      </p>
      <p class="contact-line">www.PELIKAR.com
        <svg viewBox="0 0 12 12"><circle cx="6" cy="6" r="5.5" fill="#e8611c"/><path d="M0.5 6h11M6 .5c-2.5 3-2.5 8 0 11M6 .5c2.5 3 2.5 8 0 11" stroke="#4a4a4c" stroke-width=".8" fill="none"/></svg>
      </p>
    </div>
  </section>

  <section class="card card--brand" aria-label="Business card, brand side">
    <div class="brand"><span class="brand-square"></span>PELIKAR HIRES</div>
    <p class="tagline">Luxury Restroom Trailers Rental and Sales<br>Weddings, Concerts, Charity, Sporting and Corp Events</p>
  </section>

</body>
</html>
```